Land Buying Company Needs Letterhead for Direct Mail Marketing to Land Owners

We are looking for a professional letterhead that we will be including in our direct mail marketing. We will be sending this to land owners who may be interested in selling or purchasing land.

The letterhead needs to be editable. Headers and footers would look nice, but we are open. We would want it to include our address, website, phone, and email info. For right now the address to use for design purposes would the following:

Address: 415 Bramwell Avenue #600
Dallas, TX 75219
Website - www.quillridgeacres.example
Email - info@quillridgeacres.example
Phone - 866-402-ACRE

I have attached our logo zip file that we just had done on Pixel Guild. Let me know what questions you have, and thank you.

```html
<!DOCTYPE html>
<html lang="en">
<head>
<meta charset="utf-8">
<title>Quillridge Acres Letterhead</title>
<link rel="stylesheet" href="https://fonts.googleapis.com/css2?family=Open+Sans:ital,wght@0,700;1,400;1,700&family=Crimson+Pro:wght@400&display=swap">
<style>
  :root {
    --bg: #e4e5e8;
    --paper: #ffffff;
    --forest: #3f6a2a;
    --leaf: #8cc63f;
    --leaf-soft: #c6e39a;
    --ink: #1d1d1d;
    --muted: #2b2b2b;
  }
  * { margin: 0; padding: 0; box-sizing: border-box; }
  html, body { width: 1200px; height: 1200px; overflow: hidden; background: var(--bg); }
  .sheet {
    position: absolute; left: 204px; top: 40px;
    width: 1016px; height: 1438px;
    transform: scale(0.7788); transform-origin: top left;
    background: var(--paper);
    box-shadow: 0 2px 10px rgba(0,0,0,0.12);
    font-family: "Open Sans", Arial, sans-serif;
    color: var(--ink);
  }
  .deco { position: absolute; left: 0; top: 0; }
  .accent-bar { position: absolute; left: 1007px; top: 0; width: 8px; height: 236px; background: var(--leaf); }
  .brand { position: absolute; left: 76px; top: 93px; display: flex; align-items: center; gap: 14px; }
  .brand-dot { width: 54px; height: 54px; border-radius: 50%; background: var(--forest); }
  .brand-name { font-weight: 700; font-size: 25px; color: var(--leaf); letter-spacing: 1px; font-style: normal; }
  .letter { position: absolute; left: 164px; top: 256px; width: 720px; font-style: italic; font-size: 18.5px; line-height: 22.6px; }
  .letter .strong { font-weight: 700; font-size: 19.5px; }
  .letter p { margin: 0; }
  .block-recipient { margin-bottom: 22px; }
  .block-sender { margin-bottom: 112px; }
  .body-para { margin-bottom: 22.6px !important; }
  .signature { width: 220px; height: 66px; margin: 22px 0 10px -4px;
    background: linear-gradient(90deg, rgba(29,29,29,0.08), rgba(29,29,29,0.02)); border-radius: 4px; }
  .role { font-size: 15.5px; }
  .contact { position: absolute; left: 96px; top: 1304px; display: flex; font-family: "Crimson Pro", Georgia, serif; font-size: 15.5px; line-height: 18.5px; color: var(--muted); }
  .contact-labels { text-align: right; padding: 10px 6px 0 0; }
  .contact-values { position: relative; padding: 10px 0 12px 7px; border-left: 1px solid var(--leaf-soft); }
  .contact-values::before, .contact-values::after { content: ""; position: absolute; left: 0; height: 1px; background: linear-gradient(90deg, var(--leaf-soft), transparent); }
  .contact-values::before { top: 0; width: 370px; }
  .contact-values::after { bottom: 0; width: 130px; }
</style>
</head>
<body>
<div class="sheet">
  <svg class="deco" width="1016" height="1438" viewBox="0 0 1016 1438" aria-hidden="true">
    <line x1="46" y1="0" x2="46" y2="500" stroke="var(--forest)" stroke-width="3"/>
    <polyline points="46,238 54,238 54,1150 27,1192 27,1090" fill="none" stroke="var(--forest)" stroke-width="2.5"/>
    <polygon points="40,500 47,480 47,870 40,890" fill="var(--forest)"/>
    <polygon points="20,900 40,858 40,1090 20,1135" fill="var(--forest)"/>
    <line x1="34" y1="1085" x2="34" y2="1398" stroke="var(--leaf)" stroke-width="3"/>
    <line x1="42" y1="1080" x2="42" y2="1342" stroke="var(--leaf)" stroke-width="2"/>
    <line x1="48" y1="1075" x2="48" y2="1280" stroke="var(--leaf)" stroke-width="1.5"/>
    <polyline points="340,112 466,112 412,177 170,177" fill="none" stroke="var(--leaf)" stroke-width="1"/>
  </svg>
  <div class="accent-bar"></div>

  <div class="brand">
    <div class="brand-dot"></div>
    <span class="brand-name">QUILLRIDGE ACRES</span>
  </div>

  <div class="letter">
    <div class="block-recipient">
      <p>To:</p>
      <p class="strong">ROLANDO T BRISCOE</p>
      <p>Customer</p>
    </div>
    <div class="block-sender">
      <p class="strong">QUILLRIDGE ACRES</p>
      <p>August 20, 2020</p>
    </div>
    <p>Dear Mr. Rolando</p>
    <p class="body-para">Lorem ipsum dolor sit amet, consectetuer adipiscing elit, sed diam nonummy nibh<br>euismod tincidunt ut laoreet dolore magna aliquam erat volutpat. Ut wisi enim ad<br>minim veniam, quis nostrud exerci tation ullamcorper suscipit lobortis nisl ut aliquip<br>ex ea commodo consequat.</p>
    <p class="body-para">Duis autem vel eum iriure dolor in hendrerit in vulputate velit esse molestie conse-<br>quat, vel illum dolore eu feugiat nulla facilisis at vero eros et accumsan et iusto odio<br>dignissim qui blandit praesent luptatum zzril delenit augue duis dolore te feugait<br>nulla facilisi. Ut wisi enim ad minim veniam, quis nostrud exerci tation ullamcorper<br>suscipit lobortis nisl ut aliquip ex ea commodo consequat.</p>
    <p class="body-para">Duis autem vel eum iriure dolor in hendrerit in vulputate velit esse molestie conse-<br>quat, vel illum dolore eu feugiat nulla facilisis at vero eros et accumsan et iusto odio<br>dignissim.</p>
    <p>Best Regard,</p>
    <div class="signature" role="img" aria-label="Handwritten signature of the account manager"></div>
    <p class="strong">MARCUS ELLWOOD</p>
    <p class="role">Account Manager</p>
  </div>

  <div class="contact">
    <div class="contact-labels">Address<br>Website<br>Email<br>Phone</div>
    <div class="contact-values">415 Bramwell Avenue #600 Dallas, TX 75219<br>www.quillridgeacres.example<br>info@quillridgeacres.example<br>866-402-ACRE</div>
  </div>
</div>
</body>
</html>
```